Motorcycle Tours Facebook Page

Wanting a fresh design for a Motorcycle Tour company running tours in Far North Queensland. Our market is city people who cant ride their own bikes that far and we look after them by picking them up at the airport, taking care of evrything, giving them a bike and gear and as a small group go riding through amazing secenery on great roads. We stop at rainforests, worl heritage sites and just enjoy a couple of days riding. We expect our audience may be all ages but probably over 40's. We want to express fun, enjoyment, good company, great food, amazing scenery. Have uploaded logo and a couple of images.

```html
<!DOCTYPE html>
<html lang="en">
<head>
<meta charset="utf-8">
<title>Ridgeline Motorcycle Tours – Facebook Cover</title>
<link rel="stylesheet" href="https://fonts.googleapis.com/css2?family=Great+Vibes&family=Roboto:wght@400;500&family=Roboto+Condensed:wght@400;500;700&display=swap">
<style>
  :root {
    --page-bg: #e4e6e9;
    --white: #ffffff;
    --orange: #f26f21;
    --navy: #233a74;
    --ink: #1d1d1d;
    --gold-top: #ffe15a;
    --gold-bottom: #f3b51a;
    --sky: #4f9ad8;
    --sea: #1fa6b0;
    --sea-deep: #0c6f86;
    --coast: #5f7a3a;
  }
  * { box-sizing: border-box; margin: 0; padding: 0; }
  html, body {
    width: 1200px; height: 1200px; overflow: hidden;
    background: var(--page-bg);
  }
  .cover {
    position: absolute; left: 15px; top: 356px;
    width: 1170px; height: 432px;
    background: var(--white);
    overflow: hidden;
  }
  .cover-shape { position: absolute; inset: 0; }

  .thumb {
    position: absolute; width: 154px; height: 103px;
    border: 4px solid var(--white);
    box-shadow: 0 2px 6px rgba(0,0,0,.35);
  }
  .thumb--bay    { left: 89px;  top: 33px;  background: linear-gradient(180deg,#8fb6d8 0%,#4d7a3f 45%,#2f6d8a 100%); }
  .thumb--hotel  { left: 257px; top: 33px;  background: linear-gradient(180deg,#9cc4e4 0%,#e9ece8 50%,#5d6b4a 100%); }
  .thumb--river  { left: 424px; top: 33px;  background: linear-gradient(180deg,#6a5b44 0%,#8d8672 55%,#4c5a4a 100%); }
  .thumb--forest { left: 89px;  top: 162px; background: linear-gradient(180deg,#a9c48a 0%,#4f6e33 55%,#8a7a5c 100%); }
  .thumb--fig    { left: 257px; top: 162px; background: linear-gradient(180deg,#6d8a4d 0%,#4a4a34 55%,#3c5a2c 100%); }
  .thumb--road   { left: 424px; top: 162px; background: linear-gradient(180deg,#6d8f4b 0%,#4e6a3b 45%,#5b5f63 100%); }

  .headline {
    position: absolute; left: 375px; top: 280px; width: 246px; height: 108px;
    color: var(--white);
  }
  .headline-amazing {
    position: absolute; left: 4px; top: 4px;
    font-family: "Great Vibes", cursive; font-size: 66px; line-height: 1;
    white-space: nowrap;
    text-shadow: 0 2px 4px rgba(0,0,0,.5);
  }
  .headline-the {
    position: absolute; left: 70px; top: 0;
    font-family: "Roboto", sans-serif; font-size: 19px; line-height: 1;
    color: var(--gold-top);
    text-shadow: 0 1px 2px rgba(0,0,0,.4);
  }
  .headline-region {
    position: absolute; left: 0; top: 78px; width: 246px; height: 28px;
    border-radius: 5px;
    background: linear-gradient(180deg, var(--gold-top), var(--gold-bottom));
    font-family: "Roboto", sans-serif; font-size: 20px; line-height: 28px;
    color: var(--navy); text-align: center;
  }

  .brand {
    position: absolute; left: 800px; top: 62px; width: 340px;
    display: flex; align-items: center; justify-content: center; gap: 10px;
  }
  .brand-dot { width: 24px; height: 24px; border-radius: 50%; background: var(--orange); flex: none; }
  .brand-name {
    font-family: "Roboto Condensed", sans-serif; font-weight: 700;
    font-size: 28px; line-height: 1.1; color: var(--orange);
    white-space: nowrap;
  }

  .services { position: absolute; left: 787px; top: 145px; list-style: none; }
  .service {
    display: flex; align-items: center; height: 51px;
    font-family: "Roboto Condensed", sans-serif; font-size: 20px;
    color: var(--ink); white-space: nowrap;
  }
  .service-icon {
    width: 40px; height: 40px; margin-right: 10px; flex: none;
    border: 2px solid var(--ink); border-radius: 50%;
    display: flex; align-items: center; justify-content: center;
  }
  .service-label { text-decoration: underline; text-underline-offset: 4px; }

  .tagline {
    position: absolute; left: 685px; top: 368px; width: 485px; height: 64px;
    background: var(--navy); color: var(--white);
    font-family: "Roboto Condensed", sans-serif; font-weight: 500; font-size: 17px;
    line-height: 23px; text-align: center;
    display: flex; align-items: center; justify-content: center;
  }
</style>
</head>
<body>
  <section class="cover">
    <svg class="cover-shape" width="1170" height="432" viewBox="0 0 1170 432">
      <defs>
        <linearGradient id="scene-fill" x1="0" y1="0" x2="0.4" y2="1">
          <stop offset="0" stop-color="var(--sky)"/>
          <stop offset="0.35" stop-color="#9cc9e6"/>
          <stop offset="0.55" stop-color="var(--sea)"/>
          <stop offset="1" stop-color="var(--sea-deep)"/>
        </linearGradient>
        <linearGradient id="coast-fill" x1="0" y1="0" x2="1" y2="0">
          <stop offset="0" stop-color="var(--coast)"/>
          <stop offset="1" stop-color="var(--coast)" stop-opacity="0"/>
        </linearGradient>
      </defs>
      <path d="M0 0 H664 C744 120 744 300 652 432 H0 Z" fill="var(--orange)"/>
      <g role="img" aria-label="Aerial photo of a turquoise bay with a forested coastline and blue sky">
        <path d="M0 0 H650 C728 120 728 300 638 432 H0 Z" fill="url(#scene-fill)"/>
        <path d="M0 140 H300 V432 H0 Z" fill="url(#coast-fill)" opacity="0.8"/>
      </g>
    </svg>

    <div class="thumb thumb--bay" role="img" aria-label="Photo of a quiet bay under green hills"></div>
    <div class="thumb thumb--hotel" role="img" aria-label="Photo of a motorcycle parked outside a white colonial hotel"></div>
    <div class="thumb thumb--river" role="img" aria-label="Photo of a crocodile on a riverbank"></div>
    <div class="thumb thumb--forest" role="img" aria-label="Photo of a boardwalk path through rainforest"></div>
    <div class="thumb thumb--fig" role="img" aria-label="Photo of a giant curtain fig tree"></div>
    <div class="thumb thumb--road" role="img" aria-label="Photo of motorcycles on a winding coastal road"></div>

    <div class="headline">
      <div class="headline-amazing">Amazing</div>
      <span class="headline-the">The</span>
      <div class="headline-region">Far North Queensland</div>
    </div>

    <div class="brand">
      <span class="brand-dot"></span>
      <span class="brand-name">Ridgeline<br>Motorcycle Tours</span>
    </div>

    <ul class="services">
      <li class="service">
        <span class="service-icon">
          <svg width="22" height="22" viewBox="0 0 24 24"><path d="M21 15v-2l-8-5V3.5a1.5 1.5 0 0 0-3 0V8l-8 5v2l8-2.5V18l-2 1.5V21l3.5-1 3.5 1v-1.5L13 18v-5.5z" fill="var(--ink)"/></svg>
        </span>
        <span class="service-label">Airports Shuttle Services</span>
      </li>
      <li class="service">
        <span class="service-icon">
          <svg width="22" height="22" viewBox="0 0 24 24"><path d="M12 21s-8-5.2-8-11a4.5 4.5 0 0 1 8-2.8A4.5 4.5 0 0 1 20 10c0 5.8-8 11-8 11z" fill="var(--ink)"/><path d="M12 9v6M9 12h6" stroke="var(--white)" stroke-width="2"/></svg>
        </span>
        <span class="service-label">Taking Care of Everything</span>
      </li>
      <li class="service">
        <span class="service-icon">
          <svg width="24" height="24" viewBox="0 0 24 24" fill="none" stroke="var(--ink)" stroke-width="1.8"><circle cx="6" cy="16" r="4"/><circle cx="18" cy="16" r="4"/><path d="M6 16l4-7h5l3 7M10 9l2 7h1"/><circle cx="14" cy="5" r="1.4" fill="var(--ink)"/></svg>
        </span>
        <span class="service-label">Bike and Gear Services</span>
      </li>
      <li class="service">
        <span class="service-icon">
          <svg width="22" height="22" viewBox="0 0 24 24"><path d="M2 20l7-11 4 6 3-4 6 9z" fill="var(--ink)"/></svg>
        </span>
        <span class="service-label">Riding Through Amazing Secenery</span>
      </li>
    </ul>

    <div class="tagline">We stop at rainforests, worl heritage sites and<br>just enjoy a couple of days riding</div>
  </section>
</body>
</html>
```